Lantern Jubilee Flyer

I need an 8.5x11 or 8.5x14 or 11x17 flyer for a benefit concert. Logo has already been designed; uploading several different versions, and you could choose which you want to use. For flyer design: something subtly musical (not a big fan of using musical symbols in the design, treble clefs, eighth notes, etc.) But something classy. I'm uploading unformatted copy, and two logos: one of the radio station that is helping to sponsor the event, and one for the organization the concert is benefitting. This is quick turnaround, so I promise to be very responsive with feedback. Thanks!

```html
<!DOCTYPE html>
<html lang="en">
<head>
<meta charset="utf-8">
<title>Lantern Jubilee Flyer</title>
<link rel="stylesheet" href="https://fonts.googleapis.com/css2?family=Montserrat:wght@700&family=Roboto+Condensed:wght@300;400;700&display=swap">
<style>
  :root {
    --stage: #eceae6;
    --teal: #2a9bb0;
    --blue: #2f86bf;
    --rose: #d98a8f;
    --sage: #a9c49a;
    --sun: #e6e05f;
    --ink: #3c4650;
    --yellow: #f2ec1c;
    --white: #ffffff;
    --grey: #555a5e;
    --line-grey: rgba(90, 95, 100, .32);
  }
  * { margin: 0; padding: 0; box-sizing: border-box; }
  html, body { width: 1200px; height: 831px; overflow: hidden; background: var(--stage); }

  .flyer {
    position: absolute; left: 331px; top: 0; width: 538px; height: 831px; overflow: hidden;
    background:
      radial-gradient(ellipse 55% 38% at 88% 22%, var(--rose), transparent 72%),
      radial-gradient(ellipse 45% 30% at 70% 45%, rgba(217,138,143,.8), transparent 70%),
      radial-gradient(ellipse 50% 32% at 55% 72%, var(--sun), transparent 70%),
      radial-gradient(ellipse 55% 40% at 78% 62%, var(--sage), transparent 75%),
      linear-gradient(165deg, var(--teal) 0%, var(--blue) 48%, var(--teal) 82%);
  }

  .title-panel {
    position: absolute; left: 16px; top: 12px; width: 540px; height: 296px;
    background: var(--white);
    border-radius: 60px 0 0 70px;
    box-shadow: 0 4px 14px rgba(0,0,0,.18);
  }
  .event-name {
    position: absolute; left: 52px; top: 100px;
    font-family: "Montserrat", sans-serif; font-weight: 700; color: var(--ink);
    font-size: 37px; line-height: 44px; letter-spacing: 1px;
  }

  .guitar-art {
    position: absolute; left: 272px; top: 192px; width: 266px; height: 512px;
    background:
      radial-gradient(ellipse 55% 30% at 45% 75%, rgba(225,232,215,.55), transparent 72%),
      linear-gradient(200deg, transparent 10%, var(--line-grey) 30%, transparent 48%),
      radial-gradient(ellipse 50% 28% at 45% 76%, var(--line-grey), transparent 78%);
  }

  .details {
    font-family: "Roboto Condensed", sans-serif; text-transform: uppercase;
    text-shadow: 1px 2px 3px rgba(0,0,0,.35); line-height: 1;
  }
  .details p { position: absolute; left: 27px; white-space: nowrap; }
  .lead { color: var(--yellow); font-weight: 300; }
  .main { color: var(--white); font-weight: 700; }
  .live   { top: 334px; font-size: 68px; letter-spacing: -1px; }
  .artist { top: 390px; font-size: 60px; letter-spacing: -1.5px; }
  .day    { top: 456px; font-size: 46px; letter-spacing: -1px; }
  .date   { top: 494px; font-size: 44px; letter-spacing: -1px; }
  .at     { top: 550px; font-size: 36px; }
  .venue  { top: 578px; font-size: 42px; letter-spacing: -1px; }
  .time   { top: 628px; font-size: 34px; letter-spacing: -.5px; color: var(--yellow); font-weight: 700; }

  .snow-band {
    position: absolute; left: 0; top: 664px; width: 538px; height: 96px;
    background: linear-gradient(to bottom, rgba(255,255,255,0), rgba(255,255,255,.55) 45%, var(--white) 92%);
  }

  .sponsors {
    position: absolute; left: 0; top: 756px; width: 538px; height: 75px; background: var(--white);
    font-family: "Roboto Condensed", sans-serif; color: var(--grey);
  }
  .sponsors-label { position: absolute; left: 104px; top: 31px; font-size: 14px; font-weight: 400; letter-spacing: .3px; }
  .sponsor-name {
    position: absolute; top: 22px; font-size: 13px; font-weight: 700; line-height: 15px;
    display: flex; align-items: center; gap: 6px;
  }
  .sponsor-shelter { left: 222px; }
  .sponsor-radio { left: 328px; }
  .sponsor-name .dot { flex: none; width: 12px; height: 12px; background: var(--grey); border-radius: 50%; }
</style>
</head>
<body>
  <main class="flyer">
    <div class="guitar-art" role="img" aria-label="Grey line drawing of a tilted electric guitar"></div>

    <div class="title-panel" role="img" aria-label="White guitar-body silhouette framing the event title"></div>
    <h1 class="event-name">MIDWINTER<br>LANTERN<br>JUBILEE</h1>

    <section class="details">
      <p class="lead live">Live Music</p>
      <p class="main artist">Artist Name</p>
      <p class="lead day">Saturday</p>
      <p class="main date">January 6</p>
      <p class="lead at">At</p>
      <p class="main venue">Music Hall</p>
      <p class="time">Starts at 8PM</p>
    </section>

    <div class="snow-band" role="img" aria-label="Border of white snowflakes fading into the footer"></div>

    <footer class="sponsors">
      <span class="sponsors-label">SPONSORED BY</span>
      <span class="sponsor-name sponsor-shelter"><span class="dot"></span>Riverbend<br>Shelter Alliance</span>
      <span class="sponsor-name sponsor-radio">Harbor<br>Classical Radio</span>
    </footer>
  </main>
</body>
</html>
```